Business Card Design Project

We are a tiling/bathroom renovation business based in Brisbane Australia and are looking to get a professional looking business card designed to promote ourselves.

We provide quality workmanship to upgrade/enhance peoples' homes.
Updates

Target Market(s)

Homeowners looking to renovate their bathrooms, or get tiling done. Mostly young adults to elderly who can spare several grand to upgrade their home

Industry/Entity Type

Business

Requirements
Must have
• A bold heading is a must: "Tiling Dorsey & Kell"
Must include these details: "ABN: 38 914 027 166", "BSA Licence: 5830172", "Bretta: 0419 238 571", "Lis: 0438 912 306", "Email: tilingdorseyandkell@mailbox-demo.com", "Let Us Set It Straight".

An abstract geometrical logo that's based around squares and straight lines/arrows because we are a tiling business and our slogan is "Let Us Set It Straight"
Nice to have
• I have attached an image of a logo design I got from markvista-demo.com, and the background from Cardloom-demo.com.au templates I really like together I just need the cut and paste look ironed out.

You are free to play around with different looks and feels but around the same theme as my sample. i.e. simple but striking, minimal but eye catching, or not maybe something unexpected could be perfect who knows?
Should not have
• Photorealism on a business card is a pet peeve. Too much detail for a teeny tiny business card. A Business card should stand out at a distance and you shouldn't have to squint to see it's detail.

```html
<!DOCTYPE html>
<html lang="en">
<head>
<meta charset="utf-8">
<title>Tiling Dorsey &amp; Kell – Business Card Options</title>
<link rel="stylesheet" href="https://fonts.googleapis.com/css2?family=Orbitron:wght@700&family=Open+Sans:wght@400&display=swap">
<style>
  :root {
    --page: #ffffff;
    --ink: #1c1c1c;
    --ink-soft: #3a3a3a;
    --tile-light: #f4f4f4;
    --tile-mid: #dedede;
    --swoosh-shadow: #bdbdbd;
    --info-panel: #cfcfcf;
    --accent: #f39a2b;
  }
  * { box-sizing: border-box; margin: 0; padding: 0; }
  html, body { width: 1200px; height: 800px; overflow: hidden; background: var(--page); }
  body { position: relative; font-family: "Open Sans", Arial, sans-serif; color: var(--ink); }

  .card { position: absolute; width: 450px; height: 266px; overflow: hidden; background: var(--tile-light); }
  .card--a { left: 122px; top: 110px; }
  .card--b { left: 647px; top: 110px; }
  .card--c { left: 122px; top: 392px; height: 296px; }
  .card--d { left: 647px; top: 392px; height: 296px; }

  .card__tiles {
    position: absolute; inset: 0;
    background: radial-gradient(ellipse at 55% 110%, var(--tile-mid) 0%, var(--tile-light) 55%, #fbfbfb 100%);
  }
  .card__swoosh { position: absolute; inset: 0; width: 100%; height: 100%; }

  .brand-mark { position: absolute; background: var(--accent); }

  .wordmark { position: absolute; font-family: "Orbitron", "Arial Black", sans-serif; font-weight: 700; color: var(--ink); white-space: nowrap; line-height: 1; }
  .slogan { position: absolute; font-family: "Orbitron", Arial, sans-serif; font-weight: 700; color: var(--ink); white-space: nowrap; }

  .licence {
    position: absolute; left: 0; width: 150px; height: 42px;
    background: var(--info-panel); padding: 10px 0 0 36px;
    font-size: 7.5px; line-height: 10px; color: var(--ink-soft);
  }
  .contact {
    position: absolute; right: 22px; text-align: right;
    font-size: 12px; line-height: 16px; color: var(--ink-soft);
  }
  .contact__email { font-size: 10.5px; display: inline-flex; align-items: center; gap: 4px; }
  .contact__email svg { width: 13px; height: 9px; }
</style>
</head>
<body>

<!-- Option A -->
<section class="card card--a">
  <div class="card__tiles" role="img" aria-label="Light grey floor tile grid in perspective"></div>
  <svg class="card__swoosh" viewBox="0 0 450 266" preserveAspectRatio="none">
    <defs><linearGradient id="shadeA" x1="0" y1="0" x2="0" y2="1"><stop offset="0" stop-color="#fff"/><stop offset="1" stop-color="var(--swoosh-shadow)"/></linearGradient></defs>
    <path d="M0,0 H450 V132 C380,112 320,170 220,170 C140,170 80,135 0,140 Z" fill="url(#shadeA)"/>
    <path d="M0,0 H450 V118 C380,98 320,150 220,150 C140,150 80,118 0,122 Z" fill="#fff"/>
  </svg>
  <div class="brand-mark" style="left:68px;top:14px;width:82px;height:82px;"></div>
  <div class="wordmark" style="left:194px;top:24px;font-size:30px;letter-spacing:4px;">TILING</div>
  <div class="wordmark" style="left:210px;top:62px;font-size:12px;">DORSEY &amp; KELL</div>
  <div class="licence" style="top:190px;">BSA Licence 5830172<br>ABN 38 914 027 166</div>
  <div class="contact" style="top:174px;">
    &#9742; Bretta: 0419 238 571 /<br>Lis: 0438 912 306<br>
    <span class="contact__email"><svg viewBox="0 0 13 9"><rect x="0.5" y="0.5" width="12" height="8" fill="none" stroke="currentColor"/><path d="M0.5,0.5 L6.5,5 L12.5,0.5" fill="none" stroke="currentColor"/></svg>tilingdorseyandkell@mailbox-demo.com</span>
  </div>
</section>

<!-- Option B -->
<section class="card card--b">
  <div class="card__tiles" role="img" aria-label="Light grey floor tile grid in perspective"></div>
  <svg class="card__swoosh" viewBox="0 0 450 266" preserveAspectRatio="none">
    <defs><linearGradient id="shadeB" x1="0" y1="0" x2="0" y2="1"><stop offset="0" stop-color="#fff"/><stop offset="1" stop-color="var(--swoosh-shadow)"/></linearGradient></defs>
    <path d="M0,0 H450 V100 C390,90 330,140 240,135 C150,132 80,110 0,118 Z" fill="url(#shadeB)"/>
    <path d="M0,0 H450 V86 C390,76 330,122 240,118 C150,114 80,96 0,102 Z" fill="#fff"/>
  </svg>
  <div class="brand-mark" style="left:34px;top:12px;width:74px;height:74px;"></div>
  <div class="wordmark" style="left:186px;top:6px;font-size:38px;">TILING</div>
  <div class="wordmark" style="left:160px;top:48px;font-size:18px;">DORSEY &amp; KELL</div>
  <div class="slogan" style="left:160px;top:70px;font-size:9px;">"Let us set it straight"</div>
  <div class="licence" style="top:190px;">BSA Licence 5830172<br>ABN 38 914 027 166</div>
  <div class="contact" style="top:174px;">
    &#9742; Bretta: 0419 238 571 /<br>Lis: 0438 912 306<br>
    <span class="contact__email"><svg viewBox="0 0 13 9"><rect x="0.5" y="0.5" width="12" height="8" fill="none" stroke="currentColor"/><path d="M0.5,0.5 L6.5,5 L12.5,0.5" fill="none" stroke="currentColor"/></svg>tilingdorseyandkell@mailbox-demo.com</span>
  </div>
</section>

<!-- Option C -->
<section class="card card--c">
  <div class="card__tiles" role="img" aria-label="Light grey floor tile grid in perspective"></div>
  <svg class="card__swoosh" viewBox="0 0 450 266" preserveAspectRatio="none">
    <defs><linearGradient id="shadeC" x1="0" y1="0" x2="0" y2="1"><stop offset="0" stop-color="#fff"/><stop offset="1" stop-color="var(--swoosh-shadow)"/></linearGradient></defs>
    <path d="M0,0 H450 V122 C390,108 340,168 240,170 C150,172 80,145 0,150 Z" fill="url(#shadeC)"/>
    <path d="M0,0 H450 V108 C390,94 340,150 240,152 C150,154 80,128 0,132 Z" fill="#fff"/>
  </svg>
  <div class="brand-mark" style="left:40px;top:38px;width:84px;height:84px;"></div>
  <div class="wordmark" style="left:186px;top:32px;font-size:38px;">TILING</div>
  <div class="wordmark" style="left:162px;top:76px;font-size:18px;">DORSEY &amp; KELL</div>
  <div class="slogan" style="left:58px;top:130px;font-size:14px;">"Let us set it straight"</div>
  <div class="licence" style="top:222px;">BSA Licence 5830172<br>ABN 38 914 027 166</div>
  <div class="contact" style="top:206px;">
    &#9742; Bretta: 0419 238 571 /<br>Lis: 0438 912 306<br>
    <span class="contact__email"><svg viewBox="0 0 13 9"><rect x="0.5" y="0.5" width="12" height="8" fill="none" stroke="currentColor"/><path d="M0.5,0.5 L6.5,5 L12.5,0.5" fill="none" stroke="currentColor"/></svg>tilingdorseyandkell@mailbox-demo.com</span>
  </div>
</section>

<!-- Option D -->
<section class="card card--d">
  <div class="card__tiles" role="img" aria-label="Light grey floor tile grid in perspective"></div>
  <svg class="card__swoosh" viewBox="0 0 450 266" preserveAspectRatio="none">
    <defs><linearGradient id="shadeD" x1="0" y1="0" x2="0" y2="1"><stop offset="0" stop-color="#fff"/><stop offset="1" stop-color="var(--swoosh-shadow)"/></linearGradient></defs>
    <path d="M0,0 H450 V112 C390,100 330,158 240,160 C150,162 80,140 0,146 Z" fill="url(#shadeD)"/>
    <path d="M0,0 H450 V98 C390,86 330,140 240,142 C150,144 80,124 0,128 Z" fill="#fff"/>
  </svg>
  <div class="brand-mark" style="right:44px;top:22px;width:72px;height:72px;"></div>
  <div class="wordmark" style="left:80px;top:44px;font-size:38px;">TILING</div>
  <div class="wordmark" style="left:54px;top:92px;font-size:18px;">DORSEY &amp; KELL</div>
  <div class="slogan" style="left:74px;top:116px;font-size:11px;">"Let us set it straight"</div>
  <div class="licence" style="top:222px;">BSA Licence 5830172<br>ABN 38 914 027 166</div>
  <div class="contact" style="top:206px;">
    &#9742; Bretta: 0419 238 571 /<br>Lis: 0438 912 306<br>
    <span class="contact__email"><svg viewBox="0 0 13 9"><rect x="0.5" y="0.5" width="12" height="8" fill="none" stroke="currentColor"/><path d="M0.5,0.5 L6.5,5 L12.5,0.5" fill="none" stroke="currentColor"/></svg>tilingdorseyandkell@mailbox-demo.com</span>
  </div>
</section>

</body>
</html>
```